Webdesign for blog, vlog and website
The designs for my website were better than what I expected when I started this contest. I knew I needed a call-to-action on my homepage, but I thought it wouldn't be possible and I didn't ask for it either. But Anselmo did it anyway. Furthermore, his design looked very good. For that reason I selected him as winner already before I should. I am very happy.

```html
<!DOCTYPE html>
<html lang="nl">
<head>
<meta charset="utf-8">
<title>Ideora – Believes and Convictions</title>
<link rel="stylesheet" href="https://fonts.googleapis.com/css2?family=Montserrat:wght@300;400;500;600;700&family=Open+Sans:wght@400;600&display=swap">
<style>
:root{
  --blue:#1414e0;
  --blue-dark:#0f0fb8;
  --hero:#5656cc;
  --hero-deep:#4646bd;
  --ink:#333;
  --muted:#8a8a8a;
  --line:#dcdcdc;
  --frame:#ececec;
  --footer:#f2f2f2;
  --white:#fff;
}
*{box-sizing:border-box;margin:0;padding:0}
html,body{width:1200px;height:2690px;overflow:hidden}
body{background:var(--frame);font-family:"Open Sans",sans-serif;color:var(--ink);position:relative}
a{text-decoration:none;color:inherit}
.page{position:absolute;left:24px;top:0;width:1152px;height:2690px;background:var(--white)}

/* header */
.site-header{position:absolute;left:0;top:0;width:1152px;height:68px;border-top:4px solid var(--blue);background:var(--white);border-bottom:1px solid var(--line)}
.brand{position:absolute;left:250px;top:14px;display:flex;align-items:center;gap:6px;font-family:"Montserrat",sans-serif;font-weight:700;font-size:19px;color:var(--blue)}
.brand-dot{width:20px;height:20px;border-radius:50%;background:var(--blue)}
.main-nav{position:absolute;left:528px;top:32px;display:flex;align-items:center;font-family:"Montserrat",sans-serif;font-size:8.5px;color:#444;letter-spacing:.2px}
.main-nav a{padding:0 11px}
.main-nav a+a::before{content:"";position:absolute}
.nav-sep{width:3px;height:3px;border-radius:50%;background:var(--blue)}
.main-nav .is-active{color:var(--blue);font-weight:600;border-bottom:1px solid var(--blue);padding-bottom:2px}
.lang-dot{width:9px;height:9px;border-radius:50%;background:#d33;margin-left:-4px}

/* hero */
.hero{position:absolute;left:0;top:68px;width:1152px;height:261px;background:linear-gradient(120deg,var(--hero) 0%,#6262d4 55%,var(--hero-deep) 100%);text-align:center;color:var(--white)}
.hero-title{position:absolute;left:0;right:0;top:76px;font-family:"Montserrat",sans-serif;font-weight:300;font-size:33px;letter-spacing:-.3px}
.hero-sub{position:absolute;left:0;right:0;top:118px;font-family:"Montserrat",sans-serif;font-size:13px;letter-spacing:3.5px}
.search{position:absolute;left:414px;top:158px;display:flex;gap:5px}
.search-input{width:207px;height:25px;background:var(--white);border-radius:2px;font-size:7px;color:#aaa;text-align:left;padding:8px 12px}
.search-btn{width:111px;height:25px;border:1.5px solid var(--white);border-radius:2px;font-family:"Montserrat",sans-serif;font-size:9px;line-height:22px}

/* filters */
.filters{position:absolute;left:0;top:329px;width:1152px;height:37px;font-family:"Montserrat",sans-serif;font-size:7.5px;color:#555}
.filter-group{position:absolute;top:15px;display:flex;align-items:center}
.filter-group a{padding:0 11px}
.filter-group a:first-child{padding-left:0}
.filter-group a+a{border-left:1px solid #bbb}
.filter-group .is-active{color:var(--blue);font-weight:600}

/* post grid */
.post-grid{position:absolute;left:0;top:366px;display:grid;grid-template-columns:repeat(6,192px);grid-template-rows:repeat(8,198px)}
.media{position:relative}
.media--green{background:linear-gradient(160deg,#25a3e8 0%,#2fb4d6 45%,#3cbb92 100%)}
.media--suit{background:linear-gradient(160deg,#aab3c0 0%,#d2a38c 45%,#1d2537 100%)}
.media--race{background:linear-gradient(170deg,#3a4c76 0%,#8c6f6a 50%,#b9363b 100%)}
.media--shirt{background:linear-gradient(180deg,#eef1f3 0%,#d9d2cc 55%,#2c7ad8 100%)}
.media--gate{background:linear-gradient(180deg,#15338c 0%,#2c4aa2 40%,#d8983a 100%)}
.media--dress{background:linear-gradient(170deg,#efedea 0%,#dcc7ae 45%,#2f63c9 100%)}
.media--spray{background:radial-gradient(ellipse at 55% 80%,#6b6b6b 0%,#1a1a1a 35%,#060606 100%)}
.media--gray{background:linear-gradient(170deg,#f3f2ef 0%,#e0cfb8 50%,#b6b6ba 100%)}
.play{position:absolute;left:50%;top:50%;width:84px;height:84px;margin:-42px 0 0 -42px;border:4px solid var(--white);border-radius:50%}
.play::after{content:"";position:absolute;left:31px;top:21px;border-left:28px solid var(--white);border-top:17px solid transparent;border-bottom:17px solid transparent}
.play::before{content:"";position:absolute;left:37px;top:31px;border-left:13px solid transparent;border-top:7px solid transparent;border-bottom:7px solid transparent;z-index:1}

.date{position:absolute;top:62px;width:55px;height:76px;background:var(--blue);color:var(--white);text-align:center;z-index:2}
.date--left{left:-8px}
.date--right{right:-8px}
.date::after{content:"";position:absolute;top:34px;border-top:6px solid transparent;border-bottom:6px solid transparent}
.date--left::after{left:-6px;border-right:6px solid var(--blue)}
.date--right::after{right:-6px;border-left:6px solid var(--blue)}
.date-month{display:block;font-family:"Montserrat",sans-serif;font-size:6.5px;text-transform:uppercase;padding:9px 4px 4px;border-bottom:1px dashed rgba(255,255,255,.7);margin:0 5px}
.date-day{display:block;font-family:"Montserrat",sans-serif;font-weight:300;font-size:31px;line-height:40px}
.media--tall .date{top:260px}

.post{padding:27px 16px 0 16px;background:var(--white)}
.post--wide{padding:27px 24px 0 24px}
.post-title{font-family:"Montserrat",sans-serif;font-weight:700;font-size:9.2px;line-height:11.5px;color:var(--blue);text-transform:uppercase;margin-bottom:10px}
.post--wide .post-title{text-align:justify;text-align-last:left}
.post p{font-size:7.6px;line-height:11.5px;color:var(--muted);text-align:justify;margin-bottom:10px}
.post-link{display:inline-flex;align-items:center;gap:6px;font-family:"Montserrat",sans-serif;font-size:8px;font-weight:500;color:var(--blue);text-transform:uppercase}
.link-icon{width:10px;height:10px;border:1px solid #888;border-radius:50%;position:relative}
.link-icon::after{content:"";position:absolute;left:2px;top:2.5px;width:3px;height:3px;border-top:1px solid #888;border-right:1px solid #888;transform:rotate(45deg)}

/* shop */
.shop{position:absolute;left:0;top:1950px;width:1152px;height:392px;text-align:center}
.shop-title{position:absolute;left:0;right:0;top:26px;font-family:"Montserrat",sans-serif;font-weight:400;font-size:29px;color:var(--blue)}
.shop-sub{position:absolute;left:0;right:0;top:64px;font-family:"Montserrat",sans-serif;font-size:12px;letter-spacing:3.5px;color:var(--blue)}
.shop-swoosh{position:absolute;left:470px;top:80px}
.products{position:absolute;left:242px;top:108px;display:grid;grid-template-columns:repeat(4,153px);column-gap:18px}
.product-img{width:130px;height:104px;margin:0 auto 12px;border-radius:4px}
.product-img--red{background:radial-gradient(circle at 35% 55%,#d43a3a 0%,#c22828 35%,#e9d6c0 36%,#fff 70%)}
.product-img--iron{background:radial-gradient(ellipse at center,#6d5b52 0%,#4a3b34 45%,#fff 72%)}
.product-img--cowboy{background:radial-gradient(ellipse at center,#5a4a42 0%,#3b2e28 40%,#fff 70%)}
.product-img--mat{background:radial-gradient(ellipse at center,#b4874f 0%,#8e6434 50%,#fff 75%)}
.product-name{font-family:"Montserrat",sans-serif;font-weight:600;font-size:10px;color:#555;margin-bottom:6px}
.product-desc{font-size:7.5px;line-height:14.5px;color:var(--muted)}
.product-price{font-family:"Montserrat",sans-serif;font-size:19px;color:var(--blue);margin-top:10px;line-height:20px}
.product-tax{font-size:6.5px;color:#666;margin-bottom:10px}
.product-btn{display:block;height:21px;border:1px solid var(--blue);font-family:"Montserrat",sans-serif;font-size:7.5px;font-weight:600;color:var(--blue);line-height:19px}

/* footer */
.site-footer{position:absolute;left:0;top:2342px;width:1152px;height:305px;background:var(--footer);border-top:3px solid var(--blue)}
.footer-label{font-family:"Montserrat",sans-serif;font-size:9px;color:#555;margin-bottom:14px;text-align:center}
.trust{position:absolute;top:52px;text-align:center}
.trust--pay{left:242px;width:210px}
.trust--ship{left:500px;width:150px}
.trust--social{left:700px;width:206px}
.badge-row{display:flex;justify-content:center;gap:4px}
.pay-badge{width:38px;height:22px;border-radius:3px;background:#dcdcdc}
.ship-badge{width:38px;height:22px;border-radius:3px;background:#e7c23a}
.ship-badge--alt{background:#c9c9c9}
.social-icon{width:18px;height:18px;border-radius:3px;background:#c7c7c7;margin:2px 10px}
.social-icon.is-active{background:var(--blue)}
.footer-divider{position:absolute;left:0;top:128px;width:1152px;height:1px;background:#dedede}
.footer-brand{position:absolute;left:242px;top:148px;display:flex;align-items:center;gap:5px;font-family:"Montserrat",sans-serif;font-weight:700;font-size:17px;color:var(--blue)}
.footer-brand .brand-dot{width:17px;height:17px}
.company{position:absolute;left:242px;top:192px;font-size:7.5px;line-height:13px;color:#555}
.company p+p{margin-top:11px}
.legal{position:absolute;left:412px;top:158px;font-size:7.5px;color:#555}
.legal h4,.newsletter h4{font-family:"Montserrat",sans-serif;font-weight:500;font-size:8.5px;line-height:12px;color:#555;margin-bottom:14px}
.legal li{list-style:none;margin-bottom:16px}
.newsletter{position:absolute;left:643px;top:158px;width:268px;font-size:7.5px;color:#555}
.newsletter-field{height:24px;background:var(--white);border:1px solid #d6d6d6;border-radius:2px;font-size:7.5px;color:#aaa;padding:7px 12px;margin-top:12px}
.newsletter-btn{position:absolute;right:0;top:98px;width:96px;height:22px;background:var(--white);border:1px solid #d6d6d6;border-radius:2px;font-family:"Montserrat",sans-serif;font-weight:600;font-size:7.5px;color:var(--blue);text-align:center;line-height:20px}
.copyright{position:absolute;left:0;top:2647px;width:1152px;height:43px;background:var(--white);font-size:7px;color:#666;text-align:center;line-height:43px}
</style>
</head>
<body>
<div class="page">

  <header class="site-header">
    <a class="brand"><span class="brand-dot"></span>Ideora</a>
    <nav class="main-nav">
      <a class="is-active">HOME</a><span class="nav-sep"></span>
      <a>BLOG</a><span class="nav-sep"></span>
      <a>VLOG</a><span class="nav-sep"></span>
      <a>FORUM</a><span class="nav-sep"></span>
      <a>ABOUT ME</a><span class="nav-sep"></span>
      <a>CONTACT</a><span class="nav-sep"></span>
      <a>SHOP</a><span class="lang-dot"></span>
    </nav>
  </header>

  <section class="hero">
    <h1 class="hero-title">Believes and Convictions</h1>
    <p class="hero-sub">WHAT'S YOUR IDEAS?</p>
    <div class="search">
      <div class="search-input">Search News or Vlog</div>
      <div class="search-btn">Search</div>
    </div>
  </section>

  <nav class="filters">
    <div class="filter-group" style="left:242px">
      <a class="is-active">ALL IDEAS</a><a>POLITICS</a><a>HEALTH</a><a>FOOD &amp; RECIPE</a><a>SPORTS</a><a>RANDOM</a>
    </div>
    <div class="filter-group" style="left:715px">
      <a class="is-active">BLOG &amp; VLOGS</a><a>ONLY VLOGS</a><a>ONLY BLOG</a>
    </div>
  </nav>

  <main class="post-grid">
    <!-- block one -->
    <div class="media media--green media--tall" role="img" aria-label="Vlog still: woman in a green dress against a blue sky" style="grid-area:1/1/3/3"><span class="play"></span><div class="date date--right"><span class="date-month">April</span><span class="date-day">02</span></div></div>
    <article class="post" style="grid-area:1/3"><h3 class="post-title">Lorem ipsum dolor sit amet, consectetur adipiscing elit</h3><p>Lorem ipsum dolor sit amet, consectetur adipiscing elit, sed do eiusmod tempor incididunt ut labore et dolore magna aliqua.</p><p>Lorem ipsum dolor sit amet, consectetur adipiscing elit, sed do eiusmod tempor incididunt ut labore et dolore magna</p><a class="post-link"><span class="link-icon"></span>Read more</a></article>
    <div class="media media--suit" role="img" aria-label="Photo: politician in a dark suit and red tie" style="grid-area:1/4"><div class="date date--left"><span class="date-month">February</span><span class="date-day">20</span></div></div>
    <article class="post" style="grid-area:1/5"><h3 class="post-title">Lorem ipsum dolor sit amet, consectetur adipiscing elit</h3><p>Lorem ipsum dolor sit amet, consectetur adipiscing elit, sed do eiusmod tempor incididunt ut labore et dolore magna aliqua.</p><p>Lorem ipsum dolor sit amet, consectetur adipiscing elit, sed do eiusmod tempor incididunt ut labore et dolore magna</p><a class="post-link"><span class="link-icon"></span>Read more</a></article>
    <div class="media media--race" role="img" aria-label="Photo: marathon runners in a city street" style="grid-area:1/6"><div class="date date--left"><span class="date-month">March</span><span class="date-day">18</span></div></div>

    <article class="post post--wide" style="grid-area:2/3/3/5"><h3 class="post-title">Lorem ipsum dolor sit amet, consectetur adipiscing elitlorem ipsum dolor sit amet, consectetur adipiscing elit</h3><p>Lorem ipsum dolor sit amet, consectetur adipiscing elit, sed do eiusmod tempor incididunt ut labore et dolore magna aliqua.</p><p>Lorem ipsum dolor sit amet, consectetur adipiscing elit, sed do eiusmod tempor incididunt ut labore et dolore magna aliqua. Lorem ipsum dolor sit amet, consectetur adipiscing elit, sed do eiusmod tempor incididunt ut labore et dolore magna aliqua. Lorem ipsum dolor sit amet, consectetur adipiscing elit, sed do eiusmod tempor incididunt ut labore et dolore magna aliqua.</p><a class="post-link"><span class="link-icon"></span>Play vlog</a></article>
    <div class="media media--shirt" role="img" aria-label="Vlog still: woman in a black shirt gesturing" style="grid-area:2/5"><div class="date date--right"><span class="date-month">April</span><span class="date-day">10</span></div></div>
    <article class="post" style="grid-area:2/6"><h3 class="post-title">Lorem ipsum dolor sit amet, consectetur adipiscing elit</h3><p>Lorem ipsum dolor sit amet, consectetur adipiscing elit, sed do eiusmod tempor incididunt ut labore et dolore magna aliqua.</p><p>Lorem ipsum dolor sit amet, consectetur adipiscing elit, sed do eiusmod tempor incididunt ut labore et dolore magna</p><a class="post-link"><span class="link-icon"></span>Play vlog</a></article>

    <article class="post" style="grid-area:3/1"><h3 class="post-title">Lorem ipsum dolor sit amet, consectetur adipiscing elit</h3><p>Lorem ipsum dolor sit amet, consectetur adipiscing elit, sed do eiusmod tempor incididunt ut labore et dolore magna aliqua.</p><p>Lorem ipsum dolor sit amet, consectetur adipiscing elit, sed do eiusmod tempor incididunt ut labore et dolore magna</p><a class="post-link"><span class="link-icon"></span>Read more</a></article>
    <div class="media media--gate" role="img" aria-label="Photo: illuminated city gate at dusk" style="grid-area:3/2"><div class="date date--left"><span class="date-month">May</span><span class="date-day">31</span></div></div>
    <article class="post post--wide" style="grid-area:3/3/4/5"><h3 class="post-title">Lorem ipsum dolor sit amet, consectetur adipiscing elitlorem ipsum dolor sit amet, consectetur adipiscing elit</h3><p>Lorem ipsum dolor sit amet, consectetur adipiscing elit, sed do eiusmod tempor incididunt ut labore et dolore magna aliqua.</p><p>Lorem ipsum dolor sit amet, consectetur adipiscing elit, sed do eiusmod tempor incididunt ut labore et dolore magna aliqua. Lorem ipsum dolor sit amet, consectetur adipiscing elit, sed do eiusmod tempor incididunt ut labore et dolore magna aliqua. Lorem ipsum dolor sit amet, consectetur adipiscing elit, sed do eiusmod tempor incididunt ut labore et dolore magna aliqua.</p><a class="post-link"><span class="link-icon"></span>Play vlog</a></article>
    <div class="media media--gray media--tall" role="img" aria-label="Vlog still: woman with long hair in a grey top, arms open" style="grid-area:3/5/5/7"><span class="play"></span><div class="date date--left" style="top:62px"><span class="date-month">June</span><span class="date-day">22</span></div></div>

    <div class="media media--dress" role="img" aria-label="Vlog still: smiling woman in a blue dress" style="grid-area:4/1"><div class="date date--right"><span class="date-month">July</span><span class="date-day">15</span></div></div>
    <article class="post" style="grid-area:4/2"><h3 class="post-title">Lorem ipsum dolor sit amet, consectetur adipiscing elit</h3><p>Lorem ipsum dolor sit amet, consectetur adipiscing elit, sed do eiusmod tempor incididunt ut labore et dolore magna aliqua.</p><p>Lorem ipsum dolor sit amet, consectetur adipiscing elit, sed do eiusmod tempor incididunt ut labore et dolore magna</p><a class="post-link"><span class="link-icon"></span>Play vlog</a></article>
    <div class="media media--spray" role="img" aria-label="Photo: spray mist against a black background" style="grid-area:4/3"><div class="date date--right"><span class="date-month">July</span><span class="date-day">10</span></div></div>
    <article class="post" style="grid-area:4/4"><h3 class="post-title">Lorem ipsum dolor sit amet, consectetur adipiscing elit</h3><p>Lorem ipsum dolor sit amet, consectetur adipiscing elit, sed do eiusmod tempor incididunt ut labore et dolore magna aliqua.</p><p>Lorem ipsum dolor sit amet, consectetur adipiscing elit, sed do eiusmod tempor incididunt ut labore et dolore magna</p><a class="post-link"><span class="link-icon"></span>Read more</a></article>

    <!-- block two -->
    <div class="media media--green media--tall" role="img" aria-label="Vlog still: woman in a green dress against a blue sky" style="grid-area:5/1/7/3"><span class="play"></span><div class="date date--right"><span class="date-month">October</span><span class="date-day">16</span></div></div>
    <article class="post" style="grid-area:5/3"><h3 class="post-title">Lorem ipsum dolor sit amet, consectetur adipiscing elit</h3><p>Lorem ipsum dolor sit amet, consectetur adipiscing elit, sed do eiusmod tempor incididunt ut labore et dolore magna aliqua.</p><p>Lorem ipsum dolor sit amet, consectetur adipiscing elit, sed do eiusmod tempor incididunt ut labore et dolore magna</p><a class="post-link"><span class="link-icon"></span>Read more</a></article>
    <div class="media media--suit" role="img" aria-label="Photo: politician in a dark suit and red tie" style="grid-area:5/4"><div class="date date--left"><span class="date-month">August</span><span class="date-day">11</span></div></div>
    <article class="post" style="grid-area:5/5"><h3 class="post-title">Lorem ipsum dolor sit amet, consectetur adipiscing elit</h3><p>Lorem ipsum dolor sit amet, consectetur adipiscing elit, sed do eiusmod tempor incididunt ut labore et dolore magna aliqua.</p><p>Lorem ipsum dolor sit amet, consectetur adipiscing elit, sed do eiusmod tempor incididunt ut labore et dolore magna</p><a class="post-link"><span class="link-icon"></span>Read more</a></article>
    <div class="media media--race" role="img" aria-label="Photo: marathon runners in a city street" style="grid-area:5/6"><div class="date date--left"><span class="date-month">September</span><span class="date-day">04</span></div></div>

    <article class="post post--wide" style="grid-area:6/3/7/5"><h3 class="post-title">Lorem ipsum dolor sit amet, consectetur adipiscing elitlorem ipsum dolor sit amet, consectetur adipiscing elit</h3><p>Lorem ipsum dolor sit amet, consectetur adipiscing elit, sed do eiusmod tempor incididunt ut labore et dolore magna aliqua.</p><p>Lorem ipsum dolor sit amet, consectetur adipiscing elit, sed do eiusmod tempor incididunt ut labore et dolore magna aliqua. Lorem ipsum dolor sit amet, consectetur adipiscing elit, sed do eiusmod tempor incididunt ut labore et dolore magna aliqua. Lorem ipsum dolor sit amet, consectetur adipiscing elit, sed do eiusmod tempor incididunt ut labore et dolore magna aliqua.</p><a class="post-link"><span class="link-icon"></span>Read more</a></article>
    <div class="media media--shirt" role="img" aria-label="Vlog still: woman in a black shirt gesturing" style="grid-area:6/5"><div class="date date--right"><span class="date-month">October</span><span class="date-day">18</span></div></div>
    <article class="post" style="grid-area:6/6"><h3 class="post-title">Lorem ipsum dolor sit amet, consectetur adipiscing elit</h3><p>Lorem ipsum dolor sit amet, consectetur adipiscing elit, sed do eiusmod tempor incididunt ut labore et dolore magna aliqua.</p><p>Lorem ipsum dolor sit amet, consectetur adipiscing elit, sed do eiusmod tempor incididunt ut labore et dolore magna</p><a class="post-link"><span class="link-icon"></span>Play vlog</a></article>

    <article class="post" style="grid-area:7/1"><h3 class="post-title">Lorem ipsum dolor sit amet, consectetur adipiscing elit</h3><p>Lorem ipsum dolor sit amet, consectetur adipiscing elit, sed do eiusmod tempor incididunt ut labore et dolore magna aliqua.</p><p>Lorem ipsum dolor sit amet, consectetur adipiscing elit, sed do eiusmod tempor incididunt ut labore et dolore magna</p><a class="post-link"><span class="link-icon"></span>Read more</a></article>
    <div class="media media--gate" role="img" aria-label="Photo: illuminated city gate at dusk" style="grid-area:7/2"><div class="date date--left"><span class="date-month">November</span><span class="date-day">24</span></div></div>
    <article class="post post--wide" style="grid-area:7/3/8/5"><h3 class="post-title">Lorem ipsum dolor sit amet, consectetur adipiscing elitlorem ipsum dolor sit amet, consectetur adipiscing elit</h3><p>Lorem ipsum dolor sit amet, consectetur adipiscing elit, sed do eiusmod tempor incididunt ut labore et dolore magna aliqua.</p><p>Lorem ipsum dolor sit amet, consectetur adipiscing elit, sed do eiusmod tempor incididunt ut labore et dolore magna aliqua. Lorem ipsum dolor sit amet, consectetur adipiscing elit, sed do eiusmod tempor incididunt ut labore et dolore magna aliqua. Lorem ipsum dolor sit amet, consectetur adipiscing elit, sed do eiusmod tempor incididunt ut labore et dolore magna aliqua.</p><a class="post-link"><span class="link-icon"></span>Play vlog</a></article>
    <div class="media media--gray media--tall" role="img" aria-label="Vlog still: woman with long hair in a grey top, arms open" style="grid-area:7/5/9/7"><span class="play"></span><div class="date date--left" style="top:62px"><span class="date-month">November</span><span class="date-day">25</span></div></div>

    <div class="media media--dress" role="img" aria-label="Vlog still: smiling woman in a blue dress" style="grid-area:8/1"><div class="date date--right"><span class="date-month">November</span><span class="date-day">28</span></div></div>
    <article class="post" style="grid-area:8/2"><h3 class="post-title">Lorem ipsum dolor sit amet, consectetur adipiscing elit</h3><p>Lorem ipsum dolor sit amet, consectetur adipiscing elit, sed do eiusmod tempor incididunt ut labore et dolore magna aliqua.</p><p>Lorem ipsum dolor sit amet, consectetur adipiscing elit, sed do eiusmod tempor incididunt ut labore et dolore magna</p><a class="post-link"><span class="link-icon"></span>Play vlog</a></article>
    <div class="media media--spray" role="img" aria-label="Photo: spray mist against a black background" style="grid-area:8/3"><div class="date date--right"><span class="date-month">December</span><span class="date-day">06</span></div></div>
    <article class="post" style="grid-area:8/4"><h3 class="post-title">Lorem ipsum dolor sit amet, consectetur adipiscing elit</h3><p>Lorem ipsum dolor sit amet, consectetur adipiscing elit, sed do eiusmod tempor incididunt ut labore et dolore magna aliqua.</p><p>Lorem ipsum dolor sit amet, consectetur adipiscing elit, sed do eiusmod tempor incididunt ut labore et dolore magna</p><a class="post-link"><span class="link-icon"></span>Read more</a></article>
  </main>

  <section class="shop">
    <h2 class="shop-title">From My Webshop</h2>
    <p class="shop-sub">NICE PRODUCTS... BEST PRICE</p>
    <svg class="shop-swoosh" width="212" height="16" viewBox="0 0 212 16" aria-hidden="true"><path d="M2 14 Q100 -2 210 4" fill="none" stroke="var(--blue)" stroke-width="2.5" stroke-linecap="round"/></svg>
    <div class="products">
      <div class="product">
        <div class="product-img product-img--red" role="img" aria-label="Product photo: red cookie stamp with wooden handle"></div>
        <h3 class="product-name">Koekjes Stamper</h3>
        <p class="product-desc">Lorem ipsum dolor sit amet, consectetur adipiscing elit, sed do eiusmod tempor incididunt ut labore et dolore magna aliqua.</p>
        <p class="product-price">€ 14,99</p><p class="product-tax">inkl. 19% MwSt.</p>
        <a class="product-btn">ADD TO CART</a>
      </div>
      <div class="product">
        <div class="product-img product-img--iron" role="img" aria-label="Product photo: cast iron welcome sign with cow motif"></div>
        <h3 class="product-name">Welkom bord Ranch koe</h3>
        <p class="product-desc">Lorem ipsum dolor sit amet, consectetur adipiscing elit, sed do eiusmod tempor incididunt ut labore et dolore magna aliqua.</p>
        <p class="product-price">€ 14,99</p><p class="product-tax">inkl. 19% MwSt.</p>
        <a class="product-btn">ADD TO CART</a>
      </div>
      <div class="product">
        <div class="product-img product-img--cowboy" role="img" aria-label="Product photo: cast iron welcome sign with cowboy motif"></div>
        <h3 class="product-name">Welkom bord Ranch cowboy</h3>
        <p class="product-desc">Lorem ipsum dolor sit amet, consectetur adipiscing elit, sed do eiusmod tempor incididunt ut labore et dolore magna aliqua.</p>
        <p class="product-price">€ 14,99</p><p class="product-tax">inkl. 19% MwSt.</p>
        <a class="product-btn">ADD TO CART</a>
      </div>
      <div class="product">
        <div class="product-img product-img--mat" role="img" aria-label="Product photo: double-sided coir doormat"></div>
        <h3 class="product-name">Deurmat dubbele boodschap</h3>
        <p class="product-desc">Lorem ipsum dolor sit amet, consectetur adipiscing elit, sed do eiusmod tempor incididunt ut labore et dolore magna aliqua.</p>
        <p class="product-price">€ 14,99</p><p class="product-tax">inkl. 19% MwSt.</p>
        <a class="product-btn">ADD TO CART</a>
      </div>
    </div>
  </section>

  <footer class="site-footer">
    <div class="trust trust--pay">
      <p class="footer-label">BEI UNS KAUFEN SIE SICHER EIN</p>
      <div class="badge-row"><span class="pay-badge"></span><span class="pay-badge"></span><span class="pay-badge"></span><span class="pay-badge"></span><span class="pay-badge"></span></div>
    </div>
    <div class="trust trust--ship">
      <p class="footer-label">UNSERE VERSANDPARTNER</p>
      <div class="badge-row"><span class="ship-badge"></span><span class="ship-badge ship-badge--alt"></span></div>
    </div>
    <div class="trust trust--social">
      <p class="footer-label">FOLGEN SIE UNS AUF SOCIAL NETWORK</p>
      <div class="badge-row"><span class="social-icon"></span><span class="social-icon is-active"></span><span class="social-icon"></span><span class="social-icon"></span><span class="social-icon"></span></div>
    </div>
    <div class="footer-divider"></div>

    <div class="footer-brand"><span class="brand-dot"></span>Ideora</div>
    <div class="company">
      <p>KVK-nummer: 40218377<br>BTW-nummer: NL803215674B01</p>
      <p>E-mail: info@ideora.nl</p>
      <p>Tel: 06-51827306</p>
    </div>
    <div class="legal">
      <h4>DE VOLGENDE OVEREENKOMSTEN<br>ZIJN VAN TOEPASSING OP DEZE WEBSITE:</h4>
      <ul><li>» Gebruikersovereenkomst.</li><li>» Privacyverklaring.</li><li>» Algemene voorwaarden.</li></ul>
    </div>
    <div class="newsletter">
      <h4>NIEUWSBRIEF IDEORA</h4>
      <p>Ja, ik wil de maandelijkse Ideora nieuwsbrief graag ontvangen</p>
      <div class="newsletter-field">Email Address</div>
      <a class="newsletter-btn">SUBSCRIBE NOW</a>
    </div>
  </footer>

  <div class="copyright">2017 © Ideora - All Rights Reserved</div>
</div>
</body>
</html>
```